Business card for communications

Need a business card for my consulting business - I work with not for profits, start ups and social enterprises on their media, communications campaigns.

Please see my website for colours, images and fonts www.morelbratton.example

Dana Morelbrat
Communications & Campaign strategist
Northport - Eastbay
M: 0498 317 026
E: dana@morelbratton.example
S: danamorelbrat
W: morelbratton.example
T: @danamorelbrat

(above is info only and can be presented any way e.g. should not have to be M for mobile - it should be an icon)
Updates

Dear designers I have updated the brief and uploaded high res images from my website for you to use. The designs so far with the use of images and icons are much better so far. Thank you I look forward to receiving your revised designs. Dana Morelbrat

Industry/Entity Type

Communications

Font styles to use
Sans Serif

Requirements
Must have
• Icons for contact details
Images from the website www.morelbratton.example
Nice to have
• Images - attached

```html
<!DOCTYPE html>
<html lang="en">
<head>
<meta charset="utf-8">
<title>Dana Morelbrat — Business Card</title>
<link rel="stylesheet" href="https://fonts.googleapis.com/css2?family=Lato:wght@300;400&display=swap">
<style>
  :root {
    --bg: #ece9e4;
    --card-dark: #2a292a;
    --card-dark-hi: #3b3a3b;
    --accent: #e3d81c;
    --accent-deep: #cfc30f;
    --card-yellow: #f3d707;
    --card-yellow-hi: #f7e24a;
    --ink: #2b2a28;
    --muted: #c9c9c9;
    --mark-grey: #5f5e5f;
    --white: #ffffff;
  }
  * { box-sizing: border-box; margin: 0; padding: 0; }
  html, body { width: 1200px; height: 1023px; overflow: hidden; }
  body {
    background: var(--bg);
    font-family: "Lato", "Helvetica Neue", Arial, sans-serif;
    position: relative;
  }
  .card {
    position: absolute;
    width: 700px;
    height: 400px;
    border-radius: 4px;
    box-shadow: 0 14px 30px rgba(0,0,0,.25);
  }
  /* Front */
  .card--front {
    left: 70px; top: 70px;
    background: var(--accent);
    padding: 12px;
  }
  .card--front .face {
    position: relative;
    width: 100%; height: 100%;
    background: linear-gradient(110deg, var(--card-dark) 0%, var(--card-dark-hi) 30%, var(--card-dark) 55%, #232223 100%);
    border-radius: 2px;
    box-shadow: inset 0 0 18px rgba(227,216,28,.35);
  }
  .front-mark {
    position: absolute; left: 26px; top: 22px;
    font-weight: 300; font-size: 18px; letter-spacing: 1px;
    color: var(--mark-grey);
  }
  .identity { position: absolute; left: 40px; top: 215px; }
  .identity__name { font-size: 22px; font-weight: 400; color: var(--accent); }
  .identity__role { font-size: 15px; font-weight: 400; color: var(--muted); margin-top: 4px; }
  .divider {
    position: absolute; left: 355px; top: 40px;
    width: 2px; height: 200px;
    background: linear-gradient(to bottom, rgba(255,255,255,0), rgba(255,255,255,.9) 60%, rgba(255,255,255,0));
    transform: rotate(-22deg);
    transform-origin: top center;
  }
  .contacts { position: absolute; left: 430px; top: 60px; list-style: none; }
  .contacts li {
    display: flex; align-items: center; gap: 12px;
    height: 38px; font-size: 15px; color: var(--accent);
  }
  .contacts li:nth-child(2) { margin-left: 10px; }
  .contacts li:nth-child(3) { margin-left: 20px; }
  .contacts li:nth-child(4) { margin-left: 30px; }
  .contacts svg { width: 18px; height: 18px; flex: none; }
  .dot { width: 14px; height: 14px; border-radius: 50%; background: var(--white); flex: none; margin: 0 2px; }

  /* Back */
  .card--back {
    left: 430px; top: 560px;
    background: #1d1c1d;
    padding: 12px;
  }
  .card--back .face {
    position: relative;
    width: 100%; height: 100%;
    background: linear-gradient(120deg, var(--card-yellow) 0%, var(--card-yellow-hi) 35%, var(--card-yellow) 65%, var(--accent-deep) 100%);
    border-radius: 2px;
  }
  .back-line {
    position: absolute; font-size: 15px; color: var(--ink);
    display: flex; align-items: center; gap: 10px;
  }
  .back-line svg { width: 16px; height: 16px; flex: none; }
  .back-line--place { left: 70px; top: 120px; }
  .back-line--mail { left: 330px; top: 200px; }
  .back-divider {
    position: absolute; left: 330px; top: 90px;
    width: 2px; height: 200px;
    background: linear-gradient(to bottom, rgba(255,255,255,0), rgba(255,255,255,.95) 50%, rgba(255,255,255,0));
    transform: rotate(60deg);
  }
  .back-mark {
    position: absolute; right: 36px; bottom: 30px;
    font-size: 26px; font-weight: 300; color: var(--white); letter-spacing: 1px;
  }
</style>
</head>
<body>
  <section class="card card--front" aria-label="Card front">
    <div class="face">
      <div class="front-mark">Dana Morelbrat</div>
      <div class="identity">
        <p class="identity__name">Dana Morelbrat</p>
        <p class="identity__role">Communications &amp; Campaign strategist</p>
      </div>
      <div class="divider"></div>
      <ul class="contacts">
        <li><span class="dot"></span>danamorelbrat</li>
        <li><span class="dot"></span>@danamorelbrat</li>
        <li>
          <svg viewBox="0 0 24 24" fill="#fff" aria-hidden="true"><path d="M6.6 10.8a15 15 0 0 0 6.6 6.6l2.2-2.2a1 1 0 0 1 1-.25 11.4 11.4 0 0 0 3.6.57 1 1 0 0 1 1 1V20a1 1 0 0 1-1 1A17 17 0 0 1 3 4a1 1 0 0 1 1-1h3.5a1 1 0 0 1 1 1c0 1.25.2 2.45.57 3.57a1 1 0 0 1-.25 1z"/></svg>
          0498 317 026
        </li>
        <li>
          <svg viewBox="0 0 24 24" fill="none" stroke="#fff" stroke-width="1.6" aria-hidden="true"><circle cx="12" cy="12" r="10"/><ellipse cx="12" cy="12" rx="4.5" ry="10"/><path d="M2 12h20M4 7h16M4 17h16"/></svg>
          morelbratton.example
        </li>
      </ul>
    </div>
  </section>

  <section class="card card--back" aria-label="Card back">
    <div class="face">
      <div class="back-line back-line--place">
        <svg viewBox="0 0 24 24" fill="#fff" aria-hidden="true"><path d="M12 3 3 12h5v9h8v-9h5z"/></svg>
        Northport - Eastbay
      </div>
      <div class="back-divider"></div>
      <div class="back-line back-line--mail">
        <svg viewBox="0 0 24 24" aria-hidden="true"><rect x="2" y="5" width="20" height="14" fill="#fff"/><path d="M2 5l10 8 10-8" fill="none" stroke="#2b2a28" stroke-width="1.5"/></svg>
        dana@morelbratton.example
      </div>
      <div class="back-mark">Dana Morelbrat</div>
    </div>
  </section>
</body>
</html>
```